依頼詳細
◆ディナーショー詳細

・鳴瀬野ガーデンホテル(かつて天皇陛下も宿泊された、格式&レトロ感のあるホテル)にて開催。ディナーはフランス料理
・ショー第1部:二胡と箏(着物ドレス着用)(和風の音楽でスタート)
第2部:二胡とピアノ(カクテルドレス)
(生命の息吹を感じる季節・コロナも明けて・自身の九死に一生を得た体験を含めて、生きる歓びを語るようなトークを交えて)
第3部:二胡とソノリカ(トレーンの長いゴージャスなドレス)
(プロジェクターを使用し、画像や動画で世界観を演出)
・紅茶コンサルタントが、コース一品ずつに合わせ、料理に合う紅茶を提供
・ホテル本館2階ラウンジからは、海に浮かぶ「竹島」の絶景が眺められる。
17時よりラウンジにて、夕陽に染まる絶景を見ながらウェルカムドリンクを嗜んでいただく。
宴会場へ移動し、18時よりショースタート。
・桜の咲く時期を選んで開催

◆デザイン要望

・上記のディナーショーがイメージできるようなデザイン
もしくは
チラシを一枚見るだけで「どんなショーなのだろう?」とディナーショーへ期待の膨らむようなデザイン
(・・・でありながら、主役がぼけないチラシ)が希望です。
記載項目
掲載内容のテキストは、添付のエクセルファイルをご参照ください。ページ内に、宣材写真のダウンロードURLも貼ってありますので、写真はそこからご使用ください。(写真の使用枚数等こだわりはありません)
サイズ
A4
ページ数
片面
希望イメージ
シンプル 複雑
単色 カラフル
暗い 明るい
日常 高級
遊び心 厳粛
未来的 伝統的
女性的 男性的
希望する色
設定なし
納品ファイル
• 高解像度JPG (.jpg)
• PNG形式 (.png)
補足説明
・もし可能でしたら、印刷(コピエールやモナリト等)入稿まで行っていただくか、入稿方法をご指南いただけると助かります。印刷費用については、別途予算を組んでおります。
・今回依頼が初めてで不慣れな点が多々あります。ご不明な点やご指摘等ありましたら、仰っていただけますようよろしくお願いいたします。
■ 選んだ理由

素敵な作品を沢山ご提案いただき、私としては絞りきれず、とても迷ってしまいました。そこで、家族やディナーショーの協力者、スタッフなど、複数の方に相談したところ、多数決で柚木様のデザインに票が集まり、決定させていただきました。全体的に優しい色味で文字も見やすく、気に入っています。

■ 提案者全員のお礼・コメント

この度は沢山のご提案をいただき、本当にありがとうございました。ご提案をいただく度に、A4用紙一枚に込められたデザインの多様性やデザイナーさんの思い、一瞬にしてインパクトを与えるチラシデザインの奥深さに感動して、何度か目が潤んでしまいました。できれば部屋に飾っておきたい作品もありましたが、そういう選択ができないのが残念です。また依頼させていただく際には、よろしくお願い致します。

```html
<!DOCTYPE html>
<html lang="ja">
<head>
<meta charset="utf-8">
<title>Spring Dinner show</title>
<link rel="stylesheet" href="https://fonts.googleapis.com/css2?family=Great+Vibes&family=Shippori+Mincho:wght@500;700;800&family=Noto+Serif+JP:wght@500;700&display=swap">
<style>
  :root {
    --pink: #e2799c;
    --pink-deep: #cf5b84;
    --pink-soft: #f6d6df;
    --ink: #4a3b40;
    --ink-soft: #6d5a61;
    --white: #ffffff;
    --stage: #7a5ea8;
  }
  * { box-sizing: border-box; margin: 0; padding: 0; }
  html, body { width: 846px; height: 1200px; overflow: hidden; }
  body { font-family: "Shippori Mincho", "Noto Serif JP", serif; color: var(--ink); }

  .flyer {
    position: relative; width: 846px; height: 1200px; overflow: hidden;
    background: linear-gradient(180deg, #f9e4ea 0%, #fdf3f5 60%, #fbe6ec 85%, #f4cfda 100%);
  }

  .artist-photo {
    position: absolute; left: 0; top: 0; width: 846px; height: 860px;
    background:
      radial-gradient(ellipse 230px 300px at 66% 36%, rgba(120,92,98,0.55) 0%, rgba(150,115,122,0.35) 45%, rgba(150,115,122,0) 100%),
      radial-gradient(ellipse 420px 460px at 62% 48%, #ead2d6 0%, #e5bfca 55%, rgba(240,210,220,0) 100%),
      linear-gradient(90deg, #f8e2e8 0%, #f1ccd7 40%, #e8b7c6 100%);
    -webkit-mask-image: linear-gradient(180deg, #000 0%, #000 78%, transparent 100%);
            mask-image: linear-gradient(180deg, #000 0%, #000 78%, transparent 100%);
  }
  .blossom-band {
    position: absolute; left: 0; bottom: 0; width: 846px; height: 200px;
    background: linear-gradient(180deg, rgba(244,207,218,0) 0%, #f3c8d5 60%, #eeb6c7 100%);
  }

  .title {
    position: absolute; left: 40px; top: 30px;
    font-family: "Great Vibes", cursive; font-size: 86px; font-weight: 400; line-height: 1;
    color: var(--pink); white-space: nowrap;
  }

  .poem {
    position: absolute; left: 262px; top: 212px; height: 210px;
    writing-mode: vertical-rl; white-space: nowrap;
    font-size: 15px; line-height: 34px; letter-spacing: 0.08em; color: var(--ink);
  }

  .performer { position: absolute; left: 690px; top: 400px; display: flex; flex-direction: row-reverse; gap: 8px; }
  .performer-role { writing-mode: vertical-rl; font-size: 16px; color: var(--pink-deep); font-weight: 700; }
  .performer-name { writing-mode: vertical-rl; font-size: 50px; font-weight: 800; letter-spacing: 0.1em; color: var(--ink); white-space: nowrap; }

  .portrait {
    position: absolute; left: 656px; top: 700px; width: 168px; height: 168px; border-radius: 50%;
    border: 4px solid var(--white); background: radial-gradient(circle at 50% 40%, #f3e7e6 0%, #e3c4cb 60%, #d6a9b8 100%);
  }
  .portrait-caption { position: absolute; left: 656px; top: 874px; width: 168px; text-align: center; font-size: 12px; color: var(--ink-soft); }

  .hotel-name-mark {
    position: absolute; left: 30px; top: 828px; width: 214px; text-align: center;
    font-size: 14px; font-weight: 700; color: var(--pink-deep); letter-spacing: 0.04em; white-space: nowrap;
  }
  .hotel-name-mark::before {
    content: ""; display: block; width: 24px; height: 24px; margin: 0 auto 6px;
    border-radius: 50%; background: var(--pink-soft);
  }

  .photo { position: absolute; left: 30px; width: 214px; border: 3px solid var(--white); }
  .photo-hotel { top: 886px; height: 112px; background: linear-gradient(180deg, #c7d6e6 0%, #a9b8a0 60%, #6f7f62 100%); }
  .photo-dining { top: 1004px; height: 84px; background: linear-gradient(180deg, #caa27c 0%, #e6d1b6 55%, #f2e6d8 100%); }
  .photo-stage { top: 1094px; height: 90px; background: linear-gradient(180deg, #3d2f5e 0%, var(--stage) 55%, #c79ad0 100%); }

  .details { position: absolute; left: 266px; top: 818px; width: 560px; line-height: 1.2; }
  .event-name { font-size: 24px; font-weight: 800; color: var(--ink); letter-spacing: 0.04em; margin-bottom: 6px; margin-left: -8px; }
  .row { display: flex; align-items: center; gap: 12px; white-space: nowrap; }
  .label {
    display: inline-block; min-width: 44px; padding: 2px 6px; font-size: 13px; text-align: center;
    background: var(--pink); color: var(--white); border-radius: 3px; font-weight: 700; line-height: 1.3;
  }
  .date { font-size: 44px; font-weight: 800; letter-spacing: 0.02em; margin: 0 0 2px; line-height: 1.15; }
  .date small { font-size: 26px; }
  .venue { font-size: 26px; font-weight: 800; margin: 0 0 8px; }
  .price { font-size: 16px; margin-bottom: 8px; }
  .price strong { font-size: 30px; font-weight: 800; }
  .note { font-size: 11px; color: var(--ink-soft); font-weight: 500; }
  .time-line { display: flex; align-items: baseline; gap: 12px; font-size: 21px; font-weight: 700; white-space: nowrap; line-height: 1.4; }
  .time-line .label { align-self: center; }
  .time-line .time { font-size: 23px; width: 84px; }
  .label-spacer { visibility: hidden; }

  .contact {
    position: absolute; left: 266px; top: 1122px; width: 556px; height: 60px;
    display: flex; align-items: center; gap: 12px;
    background: rgba(255,255,255,0.85); border-radius: 6px; padding: 0 16px;
  }
  .contact-label { font-size: 14px; font-weight: 700; color: var(--white); background: var(--pink-deep); padding: 4px 8px; border-radius: 3px; white-space: nowrap; }
  .contact-body { display: flex; align-items: baseline; gap: 14px; white-space: nowrap; }
  .phone { display: flex; align-items: center; gap: 6px; font-family: "Noto Serif JP", serif; font-size: 28px; font-weight: 700; }
  .url { font-size: 12px; color: var(--ink-soft); letter-spacing: 0.02em; }
</style>
</head>
<body>
<main class="flyer">
  <div class="artist-photo" role="img" aria-label="二胡を構える奏者の写真、淡い桜色の背景"></div>
  <div class="blossom-band" role="img" aria-label="裾に広がる桜の花の装飾"></div>

  <h1 class="title">Spring Dinner show</h1>

  <p class="poem">咲き誇るさくら<br>夕暮れに染まる竹島<br>悠久の時を紡ぐ二胡の調べが<br>あなたを別世界へ誘います</p>

  <div class="performer">
    <span class="performer-role">【二胡奏者】</span>
    <span class="performer-name">早瀬 澄奈</span>
  </div>

  <div class="portrait" role="img" aria-label="二胡奏者の宣材写真"></div>
  <p class="portrait-caption">[Hayase Sumina]</p>

  <div class="hotel-name-mark">鳴瀬野ガーデンホテル</div>
  <div class="photo photo-hotel" role="img" aria-label="ホテル本館の外観写真"></div>
  <div class="photo photo-dining" role="img" aria-label="宴会場のディナーテーブル写真"></div>
  <div class="photo photo-stage" role="img" aria-label="紫の照明に照らされたステージ写真"></div>

  <section class="details">
    <h2 class="event-name">【スプリングディナーショー】</h2>
    <div class="row"><span class="label">日時</span></div>
    <p class="date">2022年4月3日<small>(日)</small></p>
    <div class="row"><span class="label">場所</span></div>
    <p class="venue">鳴瀬野ガーデンホテル</p>
    <div class="row price"><span class="label">料金</span><span>お一人様 <strong>¥27,000</strong></span><span class="note">(税・サービス料込)</span></div>
    <div class="time-line"><span class="label">時間</span><span class="time">17:00〜</span><span>ウェルカムドリンク</span><span class="note">※本館2階ラウンジ</span></div>
    <div class="time-line"><span class="label label-spacer">時間</span><span class="time">18:00〜</span><span>ショー&amp;ディナー</span><span class="note">※宴会場</span></div>
  </section>

  <div class="contact">
    <span class="contact-label">お問合せ</span>
    <div class="contact-body">
      <span class="phone">
        <svg width="24" height="24" viewBox="0 0 24 24" aria-hidden="true"><path fill="#4a3b40" d="M6.6 10.8a15.1 15.1 0 0 0 6.6 6.6l2.2-2.2c.3-.3.7-.4 1-.2 1.1.4 2.3.6 3.6.6.6 0 1 .4 1 1V20c0 .6-.4 1-1 1A17 17 0 0 1 3 4c0-.6.4-1 1-1h3.5c.6 0 1 .4 1 1 0 1.3.2 2.5.6 3.6.1.3 0 .7-.2 1z"/></svg>
        (080) 5512-3408
      </span>
      <span class="url">sumina-hayase.com/contact/</span>
    </div>
  </div>
</main>
</body>
</html>
```